One business card required with 2 company logos and 2 people's details

One business card required.
No preference on design - One side could show the 2 different business logos for the companies we own. The reverse could have the details shown below.
Another option could be one business one side and one business on the reverse. Happy to receive designs.

Carol Denbigh
07700 318 274
Rachel Tolland
07700 582 036

website: truelymarvellous.example
email: info@truelymarvellous.example

website: ironwillowevents.example
email: info@ironwillowevents.example

May be nice to have icons instead of the words email/website?

I have included different versions of the logos to help with your design.

Contact Information for Business Card

see project overview

Requirements
Must have
• both company logos, both contact names and contact details

```html
<!DOCTYPE html>
<html lang="en">
<head>
<meta charset="utf-8">
<title>Business Cards – Iron Willow Events &amp; Truely Marvellous</title>
<link href="https://fonts.googleapis.com/css2?family=Roboto:wght@400;500;700&display=swap" rel="stylesheet">
<style>
  :root {
    --backdrop: #1d1d1d;
    --card-white: #ffffff;
    --blue-deep: #0a5cc0;
    --blue-light: #06b6ea;
    --blue-stripe: #1667e6;
    --slate: #43405f;
    --slate-dark: #34314d;
    --violet: #7b55e6;
    --teal: #33c8d8;
    --ink-navy: #2a2850;
    --text-on-dark: #ffffff;
  }
  * { margin: 0; padding: 0; box-sizing: border-box; }
  html, body {
    width: 1200px; height: 1200px; overflow: hidden;
    background: var(--backdrop);
    font-family: "Roboto", Arial, sans-serif;
  }
  .canvas { position: relative; width: 1200px; height: 1200px; }
  .card-slot {
    position: absolute; left: 262px;
    width: 686px; height: 392px;
  }
  .card-slot--front { top: 165px; }
  .card-slot--back { top: 653px; }
  .card {
    position: relative;
    width: 800px; height: 457px;
    transform: scale(0.8575);
    transform-origin: top left;
    background: var(--card-white);
    border-radius: 26px;
    overflow: hidden;
    box-shadow: 0 22px 40px rgba(0,0,0,0.55);
  }
  .card__wave { position: absolute; inset: 0; width: 800px; height: 457px; }
  .contacts {
    position: absolute; left: 49px; top: 34px;
    color: var(--text-on-dark);
  }
  .contact__name { font-size: 29px; font-weight: 700; line-height: 1.2; }
  .contact__phone {
    display: flex; align-items: center; gap: 6px;
    font-size: 19px; font-weight: 500; margin-top: 1px; padding-left: 2px;
  }
  .contact__phone svg { width: 16px; height: 16px; fill: currentColor; }
  .contact + .contact { margin-top: 10px; }
  .contacts__links { margin-top: 12px; font-size: 19px; line-height: 23px; padding-left: 2px; }
  .brand {
    position: absolute; left: 490px; width: 280px;
    text-align: center; font-family: "Roboto", Arial, sans-serif;
  }
  .brand--events {
    top: 262px; color: var(--blue-stripe);
    font-size: 30px; font-weight: 500; letter-spacing: 2px; line-height: 1.2;
  }
  .brand--marvellous {
    top: 258px; color: var(--ink-navy);
    font-size: 34px; font-weight: 500; line-height: 1.2;
  }
</style>
</head>
<body>
<main class="canvas">

  <section class="card-slot card-slot--front">
    <article class="card card--events">
      <svg class="card__wave" viewBox="0 0 800 457" aria-hidden="true">
        <defs>
          <radialGradient id="blueGlow" cx="52%" cy="25%" r="70%">
            <stop offset="0" stop-color="var(--blue-light)"/>
            <stop offset="1" stop-color="var(--blue-deep)"/>
          </radialGradient>
        </defs>
        <path d="M0,0 H800 V14 C760,12 700,18 640,45 C520,100 420,255 300,290 C230,310 120,290 0,230 Z" fill="url(#blueGlow)"/>
        <path transform="translate(0,20)" d="M0,230 C120,290 230,310 300,290 C420,255 520,100 640,45 C700,18 760,12 800,14" fill="none" stroke="var(--blue-stripe)" stroke-width="2.5"/>
        <path transform="translate(8,36)" d="M0,230 C120,290 230,310 300,290 C420,255 520,100 640,45 C700,18 760,12 800,14" fill="none" stroke="var(--blue-stripe)" stroke-width="6"/>
      </svg>
      <div class="contacts">
        <div class="contact">
          <p class="contact__name">Rachel Tolland</p>
          <p class="contact__phone"><svg viewBox="0 0 24 24"><path d="M6.6 10.8a15.1 15.1 0 0 0 6.6 6.6l2.2-2.2a1 1 0 0 1 1-.25 11.4 11.4 0 0 0 3.6.57 1 1 0 0 1 1 1V20a1 1 0 0 1-1 1A17 17 0 0 1 3 4a1 1 0 0 1 1-1h3.5a1 1 0 0 1 1 1c0 1.25.2 2.45.57 3.57a1 1 0 0 1-.25 1z"/></svg>07700 582 036</p>
        </div>
        <div class="contact">
          <p class="contact__name">Carol Denbigh</p>
          <p class="contact__phone"><svg viewBox="0 0 24 24"><path d="M6.6 10.8a15.1 15.1 0 0 0 6.6 6.6l2.2-2.2a1 1 0 0 1 1-.25 11.4 11.4 0 0 0 3.6.57 1 1 0 0 1 1 1V20a1 1 0 0 1-1 1A17 17 0 0 1 3 4a1 1 0 0 1 1-1h3.5a1 1 0 0 1 1 1c0 1.25.2 2.45.57 3.57a1 1 0 0 1-.25 1z"/></svg>07700 318 274</p>
        </div>
        <p class="contacts__links">info@ironwillowevents.example<br>www.ironwillowevents.example</p>
      </div>
      <p class="brand brand--events">IRON WILLOW<br>EVENTS</p>
    </article>
  </section>

  <section class="card-slot card-slot--back">
    <article class="card card--marvellous">
      <svg class="card__wave" viewBox="0 0 800 457" aria-hidden="true">
        <defs>
          <linearGradient id="violetTeal" x1="0" y1="1" x2="1" y2="0">
            <stop offset="0" stop-color="var(--teal)"/>
            <stop offset="0.45" stop-color="var(--violet)"/>
            <stop offset="0.75" stop-color="var(--blue-stripe)"/>
            <stop offset="1" stop-color="var(--teal)"/>
          </linearGradient>
        </defs>
        <path d="M0,0 H800 V14 C760,12 700,18 640,45 C520,100 420,255 300,290 C230,310 120,290 0,230 Z" fill="var(--slate)"/>
        <path transform="translate(0,20)" d="M0,230 C120,290 230,310 300,290 C420,255 520,100 640,45 C700,18 760,12 800,14" fill="none" stroke="var(--slate-dark)" stroke-width="2.5"/>
        <path transform="translate(8,36)" d="M0,230 C120,290 230,310 300,290 C420,255 520,100 640,45 C700,18 760,12 800,14" fill="none" stroke="url(#violetTeal)" stroke-width="6"/>
      </svg>
      <div class="contacts">
        <div class="contact">
          <p class="contact__name">Rachel Tolland</p>
          <p class="contact__phone"><svg viewBox="0 0 24 24"><path d="M6.6 10.8a15.1 15.1 0 0 0 6.6 6.6l2.2-2.2a1 1 0 0 1 1-.25 11.4 11.4 0 0 0 3.6.57 1 1 0 0 1 1 1V20a1 1 0 0 1-1 1A17 17 0 0 1 3 4a1 1 0 0 1 1-1h3.5a1 1 0 0 1 1 1c0 1.25.2 2.45.57 3.57a1 1 0 0 1-.25 1z"/></svg>07700 582 036</p>
        </div>
        <div class="contact">
          <p class="contact__name">Carol Denbigh</p>
          <p class="contact__phone"><svg viewBox="0 0 24 24"><path d="M6.6 10.8a15.1 15.1 0 0 0 6.6 6.6l2.2-2.2a1 1 0 0 1 1-.25 11.4 11.4 0 0 0 3.6.57 1 1 0 0 1 1 1V20a1 1 0 0 1-1 1A17 17 0 0 1 3 4a1 1 0 0 1 1-1h3.5a1 1 0 0 1 1 1c0 1.25.2 2.45.57 3.57a1 1 0 0 1-.25 1z"/></svg>07700 318 274</p>
        </div>
        <p class="contacts__links">info@truelymarvellous.example<br>www.truelymarvellous.example</p>
      </div>
      <p class="brand brand--marvellous">Truely<br>Marvellous</p>
    </article>
  </section>

</main>
</body>
</html>
```